childcare program (nursery, preschool, pre-k, and afterschool)

Please, make my website WAY better: brambleweekids.org.
I'm looking for something clean, simple, but impactful that says, "We love child care, because after 20 years, we really do!" Basically, a website that peaks your interest enough to bring you child to. We serve newborns to 12 yr olds, If you take a look at the website you can get an idea of what we use to attract the different age groups. Please be aware that I am open to suggestions.

Target Market(s)

Parents of newborn to 12 year olds

Industry/Entity Type

Childcare

Coding

Coded - Design and coding required

Number of Pages Required

5+ page

Requirements
Must have
• An upgrade to our website that nothing short of an overhaul.
Id like to have an option to have current customers login to pay their tuition. Link to our Chatterloom.
Nice to have
• Something Innovative and different, up to date features in web design.
Something fun and interactive. Think Tobrello from Fennoraldo or Dapple Wisp from Rollo Vane. Also, Testimonials
Should not have
• Traditional, boring

```html
<!DOCTYPE html>
<html lang="en">
<head>
<meta charset="utf-8">
<title>Bramblewee Kids – Child Care</title>
<link href="https://fonts.googleapis.com/css2?family=Montserrat:wght@700;800&family=Lato:ital,wght@0,400;0,700;1,700&display=swap" rel="stylesheet">
<style>
:root{
  --navy:#0d2c45;
  --teal:#2bb3ac;
  --pink:#e3124e;
  --ink:#1f2a36;
  --grey:#f3f4f6;
  --line:#d5d8dc;
  --white:#ffffff;
}
*{box-sizing:border-box;margin:0;padding:0}
html,body{width:1200px;height:5362px;overflow:hidden;background:var(--white)}
body{position:relative;font-family:"Lato",sans-serif;color:var(--ink)}
.abs{position:absolute}
h2,h3,.headline{font-family:"Montserrat",sans-serif;font-weight:800}
.photo{position:absolute}

/* header */
.nav{position:absolute;top:30px;height:40px;display:flex;align-items:center;gap:36px;font-size:12px;font-weight:700;color:var(--navy);text-transform:uppercase;z-index:3}
.nav-left{left:75px}
.nav-right{left:770px}
.nav .active{background:var(--pink);color:var(--white);padding:12px 24px;border-radius:22px}
.members{border:2px solid var(--teal);color:var(--teal);padding:10px 22px;border-radius:22px;font-size:11px}
.brand{position:absolute;left:490px;top:12px;width:220px;height:220px;border-radius:50%;background:var(--white);display:flex;align-items:center;justify-content:center;flex-direction:column;z-index:4}
.brand-mark{width:120px;height:120px;border-radius:50%;background:var(--navy);margin-bottom:8px}
.brand-name{font-family:"Montserrat",sans-serif;font-weight:800;font-size:17px;color:var(--navy)}

/* hero */
.hero-photo{left:0;top:96px;width:1200px;height:760px;background:linear-gradient(160deg,#7d8a7c,#a77f78 45%,#59627a)}
.hero-title{position:absolute;top:330px;left:0;width:1200px;text-align:center;color:var(--white);font-size:44px;line-height:52px;text-transform:uppercase}
.dots{position:absolute;display:flex;gap:8px}
.dots span{width:10px;height:10px;border-radius:50%;background:var(--teal)}
.dots .on{background:var(--pink)}

/* mission */
.section-title{font-size:52px;color:var(--navy);text-transform:uppercase;letter-spacing:.5px}
.body-text{font-size:13.5px;line-height:25px}
.pillars{position:absolute;left:75px;top:1102px;width:520px;display:grid;grid-template-columns:repeat(3,152px);gap:22px 28px}
.pillar{height:138px;border:1px solid var(--line);box-shadow:0 2px 6px rgba(0,0,0,.08);display:flex;flex-direction:column;align-items:center;justify-content:flex-end;padding-bottom:16px;font-size:16px;text-align:center;line-height:20px;color:var(--navy)}
.pillar svg{margin-bottom:14px}
.chev{position:absolute;left:578px;top:1448px;width:42px;height:42px;border:2px solid var(--navy);border-radius:50%;display:flex;align-items:center;justify-content:center}

/* buttons */
.btn{display:inline-block;font-size:13px;font-weight:700;text-transform:uppercase;padding:11px 22px;border-radius:22px}
.btn-teal{background:var(--teal);color:var(--white)}
.btn-outline{border:2px solid var(--pink);color:var(--pink);padding:9px 20px}
.btn-pink{background:var(--pink);color:var(--white)}

/* programs */
.program{position:absolute;width:520px;height:220px}
.program-ring{position:absolute;left:0;top:0;width:220px;height:220px}
.program-text{position:absolute;left:242px;top:6px;width:280px}
.program-text h3{font-size:24px;color:var(--navy);text-transform:uppercase;margin-bottom:10px}
.program-text p{font-size:13.5px;line-height:27px;margin-bottom:18px}

/* form */
.contact-item{position:absolute;display:flex;align-items:center;gap:18px;font-size:16px;line-height:25px;color:var(--navy)}
.contact-icon{width:60px;height:60px;border-radius:50%;border:2px solid var(--line);display:flex;align-items:center;justify-content:center;background:var(--white)}
.field{position:absolute}
.field label{display:block;font-size:16px;color:var(--ink);margin-bottom:12px}
.field .input{height:70px;background:var(--white);border:1px solid var(--line);font-size:13px;color:#9aa3ab;padding:26px 22px}
.field .area{height:190px;padding-top:26px}

/* footer */
.footer-nav{position:absolute;top:5227px;left:0;width:1200px;display:flex;justify-content:center;gap:48px;color:var(--white);font-size:14px;font-weight:700;text-transform:uppercase}
</style>
</head>
<body>

<!-- hero -->
<div class="photo hero-photo" role="img" aria-label="Group photo of cheering children with balloons outdoors"></div>
<div class="abs" style="left:0;top:0;width:1200px;height:96px;background:var(--white)"></div>
<nav class="nav nav-left"><span class="active">Home</span><span>Mission</span><span>Programs</span><span>Gallery</span></nav>
<nav class="nav nav-right"><span>Videos</span><span>Contact Us</span><span class="members">Members Login</span></nav>
<div class="brand"><div class="brand-mark"></div><div class="brand-name">Bramblewee Kids</div></div>
<h1 class="headline hero-title">We love child care, because after<br>20 years, we really do!</h1>
<div class="dots" style="left:564px;top:633px"><span class="on"></span><span></span><span></span><span></span></div>
<svg class="abs" style="left:0;top:650px" width="1200" height="320" viewBox="0 0 1200 320">
  <path d="M0 190 C150 230 300 160 480 150 C700 140 820 40 1000 40 C1100 40 1170 60 1200 70 L1200 320 L0 320 Z" fill="var(--teal)"/>
  <path d="M0 200 C120 240 260 200 420 190 C620 180 720 240 860 250 C1000 260 1110 230 1200 250 L1200 320 L0 320 Z" fill="var(--white)"/>
</svg>

<!-- mission -->
<h2 class="section-title abs" style="left:75px;top:922px">Our Mission</h2>
<p class="body-text abs" style="left:75px;top:998px;width:530px">We believe that every child is unique and we believe that success and growth come from encouragement and praise. Our teachers focus on building every child's self esteem and confidence through P.A.U.S.E:</p>
<div class="pillars">
  <div class="pillar"><svg width="64" height="64" viewBox="0 0 64 64" fill="none" stroke="var(--navy)" stroke-width="2"><circle cx="24" cy="12" r="5"/><path d="M24 18v20M14 28h20M24 38l-8 14M24 38l8 14M40 20v30M6 56h52"/></svg>Physical Play</div>
  <div class="pillar"><svg width="64" height="64" viewBox="0 0 64 64" fill="none" stroke="var(--navy)" stroke-width="2"><path d="M8 56V24L32 8l24 16v32Z"/><rect x="16" y="28" width="8" height="8"/><rect x="40" y="28" width="8" height="8"/><rect x="27" y="40" width="10" height="16"/></svg>Academia</div>
  <div class="pillar"><svg width="64" height="64" viewBox="0 0 64 64" fill="none" stroke="var(--navy)" stroke-width="2"><circle cx="20" cy="14" r="6"/><circle cx="44" cy="18" r="5"/><path d="M12 58V30h16v28M36 58V34h16v24"/><path d="M32 6l2 3 3-1-1 3" stroke="var(--pink)"/></svg>Unconditional<br>Love</div>
  <div class="pillar"><svg width="64" height="64" viewBox="0 0 64 64" fill="none" stroke="var(--navy)" stroke-width="2"><path d="M32 6l18 7v14c0 12-8 20-18 24-10-4-18-12-18-24V13Z"/><path d="M32 20v14M25 27h14" stroke="var(--pink)"/><path d="M6 54h20l10 4h22"/></svg>Safety</div>
  <div class="pillar"><svg width="64" height="64" viewBox="0 0 64 64" fill="none" stroke="var(--navy)" stroke-width="2"><rect x="16" y="8" width="32" height="38"/><path d="M22 18h20M22 26h20M22 34h14M8 50h48v6H8Z"/></svg>Edification</div>
</div>
<svg class="abs" style="left:610px;top:860px" width="560" height="560" viewBox="0 0 560 560">
  <path d="M280 8 A272 272 0 1 1 120 60" fill="none" stroke="var(--navy)" stroke-width="18"/>
  <path d="M140 520 A262 262 0 0 1 90 90" fill="none" stroke="#2a2a2a" stroke-width="26"/>
  <path d="M470 110 A240 240 0 0 1 420 480" fill="none" stroke="#5a5a5a" stroke-width="22"/>
  <circle cx="280" cy="280" r="218" fill="var(--white)"/>
</svg>
<div class="photo" style="left:692px;top:942px;width:396px;height:396px;border-radius:50%;background:radial-gradient(circle at 50% 60%,#c7dc3a,#5d6a48 60%,#39405a)" role="img" aria-label="Children in bright yellow camp shirts indoors"></div>
<div class="chev"><svg width="18" height="18" viewBox="0 0 18 18" fill="none" stroke="var(--navy)" stroke-width="2"><path d="M4 3l5 5 5-5M4 9l5 5 5-5"/></svg></div>

<!-- what we do -->
<svg class="abs" style="left:0;top:1495px" width="1200" height="750" viewBox="0 0 1200 750">
  <path d="M0 100 C200 60 280 130 420 90 C620 30 900 40 1080 20 C1140 12 1180 0 1200 0 L1200 750 L0 750 Z" fill="var(--navy)"/>
</svg>
<svg class="photo" style="left:0;top:1620px" width="590" height="555" viewBox="0 0 590 555" role="img" aria-label="Smiling teacher beside a boy with face paint">
  <defs><linearGradient id="wg" x1="0" y1="0" x2="1" y2="1"><stop offset="0" stop-color="#5b6a3e"/><stop offset=".5" stop-color="#c89a7c"/><stop offset="1" stop-color="#3b7fc2"/></linearGradient></defs>
  <path d="M0 10 C150 -10 420 10 560 20 C470 140 590 300 540 440 C500 540 300 560 180 540 C90 520 40 420 0 380 Z" fill="url(#wg)"/>
</svg>
<h2 class="abs" style="left:634px;top:1683px;font-size:50px;color:var(--white)">WHAT WE DO?</h2>
<p class="body-text abs" style="left:634px;top:1760px;width:490px;color:var(--white)">We strive to provide a safe learning environment that will inspire each child in our care to explore and grow at his or her own pace.<br>Our team of administrators, teachers, and caregivers spend time nurturing your children's strengths while encouraging them to reach new heights.</p>
<span class="btn btn-teal abs" style="left:634px;top:1913px">Read More</span>
<div class="abs" style="left:615px;top:2030px;font-size:22px;font-weight:700;color:var(--white)">See for yourself!</div>
<svg class="abs" style="left:668px;top:2080px" width="130" height="80" viewBox="0 0 130 80" fill="none" stroke="var(--white)" stroke-width="3"><path d="M4 6 C30 50 70 66 118 62"/><path d="M100 46l18 16-20 12"/></svg>
<div class="photo" style="left:828px;top:2007px;width:298px;height:188px;border-radius:8px;background:linear-gradient(120deg,#c38fb4,#8fa6d6)" role="img" aria-label="Summer camp video thumbnail"></div>
<div class="abs" style="left:955px;top:2079px;width:46px;height:46px;border-radius:50%;background:var(--pink)"></div>
<svg class="abs" style="left:970px;top:2091px" width="20" height="22" viewBox="0 0 20 22"><path d="M2 2l16 9-16 9Z" fill="var(--white)"/></svg>

<!-- programs -->
<h2 class="section-title abs" style="left:72px;top:2288px">Programs</h2>
<p class="abs" style="left:75px;top:2372px;font-size:13.5px">Click Programsfor a full range of classes that foster your child's individual growth</p>

<div class="program" style="left:75px;top:2435px">
  <svg class="program-ring" viewBox="0 0 220 220"><path d="M110 4 A106 106 0 1 0 216 110" fill="none" stroke="var(--navy)" stroke-width="14"/><circle cx="114" cy="110" r="96" fill="var(--teal)"/><circle cx="114" cy="110" r="86" fill="var(--white)"/><circle cx="114" cy="110" r="80" fill="#8a5a44"/></svg>
  <div class="program-text"><h3>Nursery</h3><p>We believe that the best place for your baby is in your arms. But being that most homes today contain two "breadwinners"</p><span class="btn btn-outline">Read More</span></div>
</div>
<div class="program" style="left:617px;top:2435px">
  <svg class="program-ring" viewBox="0 0 220 220"><path d="M110 4 A106 106 0 1 0 216 110" fill="none" stroke="var(--navy)" stroke-width="14"/><circle cx="114" cy="110" r="96" fill="var(--teal)"/><circle cx="114" cy="110" r="86" fill="var(--white)"/><circle cx="114" cy="110" r="80" fill="#b79a8a"/></svg>
  <div class="program-text"><h3>Preschoolers</h3><p>As your child grows, so does his curiosity meter. Your toddler absorbs information like a sponge at this stage.</p><span class="btn btn-outline">Read More</span></div>
</div>
<div class="program" style="left:75px;top:2703px">
  <svg class="program-ring" viewBox="0 0 220 220"><path d="M110 4 A106 106 0 1 0 216 110" fill="none" stroke="var(--navy)" stroke-width="14"/><circle cx="114" cy="110" r="96" fill="var(--teal)"/><circle cx="114" cy="110" r="86" fill="var(--white)"/><circle cx="114" cy="110" r="80" fill="#9c4b4b"/></svg>
  <div class="program-text"><h3>Pre-K</h3><p>Our Pre-Kers never stop expoloring, and are introduced to problem-solving concepts that involve math and science.</p><span class="btn btn-outline">Read More</span></div>
</div>
<div class="program" style="left:617px;top:2703px">
  <svg class="program-ring" viewBox="0 0 220 220"><path d="M110 4 A106 106 0 1 0 216 110" fill="none" stroke="var(--navy)" stroke-width="14"/><circle cx="114" cy="110" r="96" fill="var(--teal)"/><circle cx="114" cy="110" r="86" fill="var(--white)"/><circle cx="114" cy="110" r="80" fill="#a88672"/></svg>
  <div class="program-text"><h3>After-School</h3><p>Our AfterSchoolers know the drill - "Do what we have to do, so we can do what we wanna do.</p><span class="btn btn-outline">Read More</span></div>
</div>

<!-- summer camp -->
<div class="abs" style="left:0;top:2995px;width:1200px;height:700px;background:var(--navy)"></div>
<svg class="photo" style="left:612px;top:3065px" width="588" height="580" viewBox="0 0 588 580" role="img" aria-label="Two young children in yellow camp shirts outdoors">
  <defs><linearGradient id="cg" x1="0" y1="0" x2="1" y2="1"><stop offset="0" stop-color="#6c6a4f"/><stop offset=".5" stop-color="#c8e23a"/><stop offset="1" stop-color="#4f6e3c"/></linearGradient></defs>
  <path d="M120 20 C240 -10 420 10 520 40 C580 60 588 120 588 160 L588 520 C520 560 420 600 300 560 C200 520 120 520 60 460 C0 380 20 300 10 220 C0 120 40 40 120 20 Z" fill="url(#cg)"/>
</svg>
<h2 class="abs" style="left:75px;top:3163px;font-size:50px;color:var(--white)">SUMMER CAMP</h2>
<p class="abs" style="left:75px;top:3243px;width:480px;font-size:31px;line-height:40px;font-style:italic;font-weight:700;color:var(--teal)">"Mommy, I'm BrambleweeSummerCamp!"</p>
<p class="body-text abs" style="left:75px;top:3346px;width:495px;color:var(--white)">At Bramblewee Summer Camp, your child's summer will be packed with fun-filled learning experiences. Your child will navigate through the universe around them through Field trips to Museums, Farms, and zoos; experience magic shows, cool down at awesome Aquatic Parks, and so much more - and all for an incredible cost!</p>
<span class="btn btn-teal abs" style="left:75px;top:3497px">Read More</span>
<svg class="abs" style="left:0;top:3600px" width="1200" height="140" viewBox="0 0 1200 140">
  <path d="M0 130 C80 70 160 60 260 70 C500 90 700 110 900 100 C1050 92 1150 60 1200 40 L1200 140 L0 140 Z" fill="var(--grey)"/>
</svg>

<!-- get in touch -->
<div class="abs" style="left:0;top:3738px;width:1200px;height:900px;background:var(--grey)"></div>
<svg class="abs" style="left:820px;top:3860px" width="380" height="560" viewBox="0 0 380 560" fill="none" stroke="#e6e8ea" stroke-width="40"><circle cx="280" cy="280" r="230"/></svg>
<h2 class="abs" style="left:0;top:3822px;width:1200px;text-align:center;font-size:48px;color:var(--navy)">GET IN TOUCH</h2>
<div class="contact-item" style="left:302px;top:3942px"><div class="contact-icon"><svg width="22" height="28" viewBox="0 0 22 28"><path d="M11 1C5 1 1 5.5 1 11c0 7 10 16 10 16s10-9 10-16C21 5.5 17 1 11 1Z" fill="none" stroke="var(--pink)" stroke-width="2.5"/><circle cx="11" cy="11" r="3.5" fill="var(--pink)"/></svg></div><div>27 Orchard Lane<br>Fairbrook, NY 11990 US<br>5550142277</div></div>
<div class="contact-item" style="left:596px;top:3942px"><div class="contact-icon"><svg width="26" height="26" viewBox="0 0 26 26"><path d="M6 2l5 6-3 3c1.5 3 4 5.5 7 7l3-3 6 5-3 4C12 24 2 14 2 5Z" fill="var(--pink)"/></svg></div><div>Phone<br>5550142277</div></div>
<div class="contact-item" style="left:815px;top:3942px"><div class="contact-icon"><svg width="28" height="20" viewBox="0 0 28 20"><rect x="1" y="1" width="26" height="18" rx="2" fill="var(--pink)"/><path d="M2 3l12 9 12-9" fill="none" stroke="var(--white)" stroke-width="2"/></svg></div><div>Email<br>hello@brambleweekids.org</div></div>
<div class="photo" style="left:0;top:3990px;width:280px;height:650px;border-radius:0 140px 0 0;background:linear-gradient(180deg,#5b3a2a,#2d77b5 55%,#e4e6ea)" role="img" aria-label="Curly-haired girl sitting with a tablet"></div>
<div class="field" style="left:302px;top:4053px;width:398px"><label>Your name</label><div class="input">John doe</div></div>
<div class="field" style="left:730px;top:4053px;width:398px"><label>Subject</label><div class="input">Nemo enim ipsam</div></div>
<div class="field" style="left:302px;top:4173px;width:398px"><label>Email address</label><div class="input">hello@brambleweekids.org</div></div>
<div class="field" style="left:730px;top:4173px;width:398px"><label>Message</label><div class="input area">Lorem ipsum dolor sit amet</div></div>
<div class="field" style="left:302px;top:4293px;width:398px"><label>Phone</label><div class="input">5550142277</div></div>
<div class="abs" style="left:605px;top:4435px;width:220px;height:54px;background:var(--pink);color:var(--white);font-weight:700;font-size:15px;display:flex;align-items:center;justify-content:center">SUBMIT</div>

<!-- testimonials / update -->
<svg class="abs" style="left:0;top:4560px" width="1200" height="520" viewBox="0 0 1200 520">
  <path d="M0 110 C150 40 300 90 500 110 C720 130 900 90 1060 70 C1130 62 1170 50 1200 40 L1200 520 L0 520 Z" fill="var(--teal)"/>
</svg>
<h2 class="abs" style="left:75px;top:4745px;font-size:34px;color:var(--white)">TESTIMONIALS</h2>
<div class="dots" style="left:476px;top:4760px"><span style="background:var(--navy)"></span><span style="background:var(--white)"></span><span style="background:var(--white)"></span><span style="background:var(--white)"></span></div>
<div class="photo" style="left:75px;top:4818px;width:150px;height:150px;border-radius:50%;border:4px solid var(--white);background:linear-gradient(160deg,#3c2a22,#9a6b50)" role="img" aria-label="Portrait of a smiling parent"></div>
<p class="abs" style="left:256px;top:4815px;width:310px;font-size:13px;line-height:26px;color:var(--white)">"   Maecenas venenatis fringilla eleifend ullam dapibus tincidunt augue sed porttitor uisque vulputate ex ut ipsum rhoncus tristique. Mauris elit eros, malesuada eu maximus in, tincidunt in dui..."</p>
<div class="abs" style="left:256px;top:4968px;font-size:13px;font-weight:700;color:var(--navy)">NAME HEADING</div>
<div class="abs" style="left:602px;top:4755px;width:2px;height:255px;background:rgba(255,255,255,.6)"></div>
<h2 class="abs" style="left:660px;top:4745px;font-size:34px;color:var(--white)">COVID-19 UPDATE</h2>
<p class="abs" style="left:660px;top:4808px;width:470px;font-size:13px;line-height:25px;color:var(--white)">Lorem ipsum dolor sit amet, consectetur adipiscing elit. Etiam dignissim ut massa in sagittis. Integer at urna sit amet ante fermentum finibus. Phasellus nec est tempor, mollis sem in, vestibulum eros fermentum ipsum.</p>
<span class="btn btn-pink abs" style="left:662px;top:4950px">Get Updates</span>

<!-- call band -->
<div class="abs" style="left:0;top:5065px;width:1200px;height:112px;background:var(--pink);color:var(--white);font-size:23px;font-weight:700;display:flex;align-items:center;justify-content:center">Call Us Today at 5550142277. Three amazing locations to serve you.</div>

<!-- footer -->
<div class="abs" style="left:0;top:5177px;width:1200px;height:185px;background:var(--navy)"></div>
<nav class="footer-nav"><span>Home</span><span>Mission</span><span>Programs</span><span>Gallery</span><span>Videos</span><span>Contact Us</span></nav>
<div class="abs" style="left:0;top:5275px;width:1200px;text-align:center;font-size:13px;color:var(--white)">Copyright © 2020 Bramblewee Kids, Inc All Rights Reserved.</div>
<div class="abs" style="left:515px;top:5305px;display:flex;gap:18px">
  <span style="width:16px;height:16px;border-radius:50%;background:var(--white)" aria-label="Chatterloom"></span>
  <span style="width:16px;height:16px;border-radius:50%;background:var(--white)" aria-label="Social link"></span>
  <span style="width:16px;height:16px;border-radius:50%;background:var(--white)" aria-label="Social link"></span>
  <span style="width:16px;height:16px;border-radius:50%;background:var(--white)" aria-label="Social link"></span>
  <span style="width:16px;height:16px;border-radius:50%;background:var(--white)" aria-label="Social link"></span>
</div>

</body>
</html>
```